Business Card 85x40mm - Freelance audio mixing / live event operator

I am a freelance audio operator working in live events. Mostly corporate events mixing sound for a range of entertainment, awards nights and functions. I need a new card to give to perspective clients.

The final design will convey bold professionalism with a general dark vibe. Looking for dark-ish background with some smatterings of colour added.

I have attatched my old BC for an idea of what I have liked in the past. Id like a more modern updated design (that circular design on the back is not my logo it is just a picture I found that resembled sound} . For an added element possibly a mixture of some playful colours in a way that resembles an audio wave form or sound.

I have attached a photo called "audio software" with some colourful squiggly lines; maybe incorporate elements of that into into design
Updates

Added extra $ to project Damn Pixel hives fees are unreasonable

Target Market(s)

Mostly corporate clients

Industry/Entity Type

Events

Contact Information for Business Card

Corwin Pellath
Sound | FOH | Monitors | Systems | Corporate

Digital Audio Mixing Specialist, Live Event Technical Professional,

corwinpellath@mailvexo.net, +61 402 918 357

Colors
ec1f27
ffc214
9bcb3c
6b449b

Requirements
Must have
• Dark theme
• 85x40mm dimensions
Nice to have
• some sort of imagery or design to reflect audio/sound

```html
<!DOCTYPE html>
<html lang="en">
<head>
<meta charset="utf-8">
<title>Corwin Pellath – Business Card</title>
<link href="https://fonts.googleapis.com/css2?family=Saira+Condensed:wght@800&family=Saira:wght@400;500&display=swap" rel="stylesheet">
<style>
  :root{
    --backdrop:#e6e7e8;
    --card:#3a3740;
    --card-deep:#2c2a31;
    --ink:#ffffff;
    --ink-soft:#e4e1ea;
    --violet:#8c5dc0;
    --violet-soft:#a982d6;
    --wave-magenta:#c23fb5;
    --wave-blue:#5f8fd6;
  }
  *{box-sizing:border-box;margin:0;padding:0}
  html,body{width:1200px;height:969px;overflow:hidden}
  body{
    background:var(--backdrop);
    display:flex;align-items:center;justify-content:center;gap:60px;
    font-family:"Saira",Arial,sans-serif;
  }
  .card{
    position:relative;width:500px;height:235px;
    background:linear-gradient(160deg,var(--card),var(--card-deep));
    box-shadow:0 6px 18px rgba(0,0,0,.18);
    overflow:hidden;
    display:flex;flex-direction:column;align-items:center;justify-content:center;
  }
  .card-front .waveform-art{
    position:absolute;inset:0;
    background:
      radial-gradient(ellipse 38% 55% at 52% 55%,rgba(95,143,214,.45),transparent 70%),
      radial-gradient(ellipse 60% 85% at 50% 50%,rgba(194,63,181,.35),transparent 75%);
  }
  .name{
    position:relative;
    font-family:"Saira Condensed","Arial Narrow",sans-serif;
    font-weight:800;letter-spacing:1.5px;text-transform:uppercase;line-height:1;
  }
  .card-front .name{color:var(--ink);font-size:50px}
  .services{position:relative;display:flex;gap:5px;margin-top:8px}
  .service{
    color:var(--ink);font-size:14px;font-weight:500;letter-spacing:.6px;text-transform:uppercase;
    border:1.5px solid var(--ink);border-radius:4px;padding:0 4px;line-height:18px;
  }
  .card-back .name{color:var(--violet);font-size:46px}
  .roles{color:var(--ink-soft);font-size:12.5px;margin-top:6px;display:flex;align-items:center;gap:6px}
  .roles .dot{width:4px;height:4px;background:var(--violet);border-radius:50%}
  .divider{width:400px;border-top:2px dotted var(--violet-soft);margin:14px 0 16px;opacity:.8}
  .contact{display:flex;align-items:center;gap:10px;color:var(--ink);font-size:21px;line-height:1.5}
  .contact svg{width:20px;height:20px;stroke:var(--violet-soft);fill:none;stroke-width:1.6}
</style>
</head>
<body>
  <section class="card card-front">
    <div class="waveform-art" role="img" aria-label="Colourful dotted audio waveform burst in magenta and blue"></div>
    <h1 class="name">Corwin Pellath</h1>
    <div class="services">
      <span class="service">Sound</span>
      <span class="service">FOH</span>
      <span class="service">Monitors</span>
      <span class="service">Systems</span>
      <span class="service">Corporate</span>
    </div>
  </section>

  <section class="card card-back">
    <h2 class="name">Corwin Pellath</h2>
    <p class="roles">Digital Audio Mixing Specialist <span class="dot"></span> Live Event Technical Professional</p>
    <div class="divider"></div>
    <p class="contact">
      <svg viewBox="0 0 24 24" aria-hidden="true"><circle cx="12" cy="12" r="10"/><path d="M9 7l1.5 3-1.3 1.2a7 7 0 0 0 3.6 3.6L14 13.5l3 1.5-.8 2a2 2 0 0 1-2 .8A9 9 0 0 1 7 10.8a2 2 0 0 1 .8-2z"/></svg>
      +61 402 918 357
    </p>
    <p class="contact">
      <svg viewBox="0 0 24 24" aria-hidden="true"><rect x="3" y="6" width="18" height="12" rx="1"/><path d="M3 6l9 7 9-7"/></svg>
      corwinpellath@mailvexo.net
    </p>
  </section>
</body>
</html>
```